Business Card Design - Brightfold Dwellings

Hi there,

We would like a business card for our new venture, Brightfold Dwellings.

We are based in Western Australia and specialise in taking tired, old properties and making them look new again. We aim to create enjoyably liveable homes for young families in particular.

Product pricing is mid range i.e. appliances, furnishings, fixtures (not top end but not cheap either)

Our work is primarily cosmetic renovation (approx. 80%) and the rest construction (approx 20%).

We would like a business card that conveys the following:
- clean, simplistic/minimalistic design
- modern, contemporary style
- a touch of funk/uniqueness
- appealing to both females and males
- professionalism

I have uploaded our logo in grey or green, I do not mind which one you choose to use (please use either coloured logo on the pure white background not the white on colour version).

Details to include on the business card are:
Names: Corina Maddox and Pete Okonbrie
Mobile: 0417 362 908
Email: info@brightfolddwellings.com.au
Website: www.brightfolddwellings.com.au (note: this website is currently being developed)
Note: We will provide final details such as mobile number and names on on selection of successful design)

On the other side of the card please include a line similar to "We buy tired, un-renovated properties and sell them looking new again!"

The business card will also need to include the following "ABN 47 219 635 104" which is our Australian Business Number (again the actual number will be provided on selection of successful design). We would like this number somewhere near our name Brightfold Dwellings but in much smaller text.

The purpose of the business cards will be to give to suppliers, real estate agents, people wanting assistance in locating a property in need of renovation and potential buyers.

Thank you and please let me know if you have any further questions.

```html
<!DOCTYPE html>
<html lang="en">
<head>
<meta charset="utf-8">
<title>Brightfold Dwellings – Business Card</title>
<link rel="stylesheet" href="https://fonts.googleapis.com/css2?family=Tinos:wght@400;700&display=swap">
<style>
  :root {
    --green: #8cbb2a;
    --ink: #1d1d1b;
    --card-white: #f6f6f4;
    --backdrop: #ecebe8;
    --white: #ffffff;
  }
  * { box-sizing: border-box; margin: 0; padding: 0; }
  html, body {
    width: 1200px;
    height: 1056px;
    overflow: hidden;
    background: var(--backdrop);
    font-family: "Tinos", "Times New Roman", serif;
  }
  .sheet { position: relative; width: 1200px; height: 1056px; }
  .card {
    position: absolute;
    left: 240px;
    width: 720px;
    height: 440px;
    overflow: hidden;
    box-shadow: 0 6px 18px rgba(0,0,0,0.12);
  }
  .card--front { top: 64px; background: var(--card-white); }
  .card--back { top: 552px; background: var(--green); }

  .front-swoosh { position: absolute; inset: 0; width: 720px; height: 440px; }

  .holder {
    position: absolute;
    left: 300px;
    top: 34px;
    color: var(--ink);
    white-space: nowrap;
  }
  .holder__name { font-size: 30px; font-weight: 700; letter-spacing: 0.3px; line-height: 36px; }
  .holder__title { font-size: 18px; line-height: 24px; }

  .contacts {
    position: absolute;
    right: 36px;
    top: 140px;
    list-style: none;
    color: var(--ink);
    font-size: 17px;
    line-height: 30px;
    white-space: nowrap;
  }
  .contacts li { display: flex; justify-content: flex-end; align-items: center; gap: 10px; }
  .contacts svg { width: 16px; height: 16px; flex: none; }

  .wordmark {
    position: absolute;
    left: 40px;
    top: 268px;
    color: var(--green);
    font-size: 30px;
    line-height: 36px;
    font-weight: 400;
    white-space: nowrap;
  }
  .abn {
    position: absolute;
    left: 150px;
    top: 330px;
    color: var(--ink);
    font-size: 13px;
    letter-spacing: 0.3px;
    white-space: nowrap;
  }

  .tagline {
    position: absolute;
    left: 0; right: 0; top: 120px;
    text-align: center;
    color: var(--white);
    font-size: 20px;
    line-height: 28px;
  }
  .wordmark--reverse {
    position: absolute;
    left: 0; right: 0; top: 210px;
    text-align: center;
    color: var(--white);
    font-size: 52px;
    font-weight: 400;
  }
</style>
</head>
<body>
<main class="sheet">

  <section class="card card--front" aria-label="Business card front">
    <svg class="front-swoosh" viewBox="0 0 720 440" aria-hidden="true">
      <path d="M134,0 C214,170 344,330 504,440 L720,440 L720,0 Z" fill="var(--ink)"/>
      <path d="M150,0 C230,170 360,330 520,440 L720,440 L720,0 Z" fill="var(--green)"/>
    </svg>

    <div class="holder">
      <p class="holder__name">Corina Maddox</p>
      <p class="holder__title">Managing Director</p>
    </div>

    <ul class="contacts">
      <li>0417 362 908
        <svg viewBox="0 0 16 16" aria-hidden="true"><rect x="4" y="1" width="8" height="14" rx="1.5" fill="none" stroke="var(--ink)" stroke-width="1.6"/><circle cx="8" cy="12.5" r="0.9" fill="var(--ink)"/></svg>
      </li>
      <li>info@brightfolddwellings.com.au
        <svg viewBox="0 0 16 16" aria-hidden="true"><rect x="1" y="3.5" width="14" height="9" fill="none" stroke="var(--ink)" stroke-width="1.5"/><path d="M1,3.5 L8,9 L15,3.5" fill="none" stroke="var(--ink)" stroke-width="1.5"/></svg>
      </li>
      <li>www.brightfolddwellings.com.au
        <svg viewBox="0 0 16 16" aria-hidden="true"><circle cx="8" cy="8" r="6.5" fill="none" stroke="var(--ink)" stroke-width="1.5"/><path d="M1.5,8 H14.5 M8,1.5 C5,5 5,11 8,14.5 M8,1.5 C11,5 11,11 8,14.5" fill="none" stroke="var(--ink)" stroke-width="1.2"/></svg>
      </li>
    </ul>

    <p class="wordmark">Brightfold Dwellings</p>
    <p class="abn">ABN 47 219 635 104</p>
  </section>

  <section class="card card--back" aria-label="Business card back">
    <p class="tagline">We buy tired, un-renovated properties<br>and sell them looking new again!</p>
    <p class="wordmark--reverse">Brightfold Dwellings</p>
  </section>

</main>
</body>
</html>
```